Business Card Design

Rubber roller servicing company. Specializing in rubber to metal bonding. Serving various industries including, pharmaceutical, textile, plastic extrusion, polythene bag converting, laminating and the food industries.

Industry/Entity Type

Plastic

Contact Information for Business Card

Garvey Cylinder & Elastomer Co Ltd, Desmond Ablewhite, Managing Director, Unit at Fernholm, Castleford Lane, Aspleby, Halverton, Westmoor Shire, HX9 2LT, Tel 01632 960418, Fax 01632 960773, email info@garveycylinder.co.uk,

```html
<!DOCTYPE html>
<html lang="en">
<head>
<meta charset="utf-8">
<title>Garvey Cylinder &amp; Elastomer Co Ltd – Business Card</title>
<link rel="stylesheet" href="https://fonts.googleapis.com/css2?family=Arimo:wght@400;700&display=swap">
<style>
  :root {
    --canvas: #e9e6e1;
    --card: #ffffff;
    --ink: #1e1e1e;
    --brown: #a5631f;
    --orange: #ee7d1c;
    --olive: #4a4a2c;
    --tab: #a9661f;
    --ghost: #fbe3da;
    --white: #ffffff;
  }
  * { box-sizing: border-box; margin: 0; padding: 0; }
  html, body { width: 1200px; height: 1200px; overflow: hidden; }
  body {
    background: var(--canvas);
    font-family: "Arimo", Arial, sans-serif;
    display: flex; align-items: center; justify-content: center;
  }
  .card {
    position: relative;
    width: 1080px; height: 660px;
    background: var(--card);
    overflow: hidden;
    box-shadow: 0 10px 30px rgba(0,0,0,.18);
  }
  .card-shapes { position: absolute; inset: 0; }
  .ghost-name {
    position: absolute; left: 70px; right: 20px; top: 90px;
    font-weight: 700; font-size: 230px; letter-spacing: 4px;
    color: var(--ghost); line-height: 1; text-align: center;
    white-space: nowrap;
  }
  .holder { position: absolute; left: 64px; top: 52px; }
  .holder-name { font-size: 36px; font-weight: 700; color: var(--ink); }
  .holder-role { font-size: 24px; font-weight: 400; color: var(--brown); margin-top: 4px; }
  .brand {
    position: absolute; right: 48px; top: 56px;
    display: flex; align-items: center; gap: 16px;
  }
  .brand-square { width: 70px; height: 70px; background: var(--orange); flex: none; }
  .brand-name {
    font-size: 30px; font-weight: 700; color: var(--ink);
    line-height: 1.1; width: 330px;
  }
  .contacts { position: absolute; left: 60px; top: 200px; list-style: none; }
  .contacts li {
    display: flex; align-items: flex-start; gap: 14px;
    font-size: 27px; font-weight: 700; color: var(--ink);
    margin-bottom: 14px; line-height: 1.3;
  }
  .contacts svg { width: 30px; height: 30px; flex: none; margin-top: 2px; fill: var(--brown); }
  .tab-label {
    position: absolute; right: 80px; top: 483px;
    font-size: 28px; font-weight: 400; color: var(--white); letter-spacing: 1px;
  }
  .services {
    position: absolute; left: 20px; right: 20px; top: 540px;
    text-align: center; color: var(--white);
    font-size: 26px; line-height: 1.22;
  }
</style>
</head>
<body>
  <article class="card">
    <svg class="card-shapes" viewBox="0 0 1080 660" aria-hidden="true">
      <polygon points="0,0 1080,0 1080,18 560,18 540,6 0,6" fill="var(--orange)"/>
      <polygon points="0,500 0,640 1080,640 1080,500" fill="var(--olive)"/>
      <polygon points="0,490 0,500 1080,500 1080,490" fill="var(--orange)"/>
      <polygon points="0,660 0,640 1080,640 1080,660" fill="var(--olive)"/>
      <polygon points="600,500 630,468 1080,468 1080,530 600,530" fill="var(--tab)"/>
    </svg>

    <div class="ghost-name" aria-hidden="true">GARVEY</div>

    <header class="holder">
      <h1 class="holder-name">Desmond Ablewhite</h1>
      <p class="holder-role">Managing Director</p>
    </header>

    <div class="brand">
      <span class="brand-square"></span>
      <span class="brand-name">Garvey Cylinder &amp; Elastomer Co Ltd</span>
    </div>

    <ul class="contacts">
      <li>
        <svg viewBox="0 0 24 24"><path d="M3 8c0-2 4-4 9-4s9 2 9 4v2h-5V8H8v2H3zM6 11h12l2 9H4z"/></svg>
        01632 960418
      </li>
      <li>
        <svg viewBox="0 0 24 24"><path d="M7 2h10a1 1 0 0 1 1 1v18a1 1 0 0 1-1 1H7a1 1 0 0 1-1-1V3a1 1 0 0 1 1-1zm1 3v7h8V5zm1 9v2h2v-2zm4 0v2h2v-2zm-4 3v2h2v-2zm4 0v2h2v-2z"/></svg>
        01632 960773
      </li>
      <li>
        <svg viewBox="0 0 24 24"><path d="M2 5h20v14H2zm2 2v.5l8 6 8-6V7zm0 3v7h16v-7l-8 6z"/></svg>
        info@garveycylinder.co.uk
      </li>
      <li>
        <svg viewBox="0 0 24 24"><path d="M12 3l10 9h-3v9h-5v-6h-4v6H5v-9H2z"/></svg>
        <span>Unit at Fernholm, Castleford Lane, Aspleby, Halverton,<br>Westmoor Shire, HX9 2LT</span>
      </li>
    </ul>

    <h2 class="tab-label">OUR SERVICE</h2>
    <p class="services">
      rubber to metal bonding | Serving various industries including<br>
      pharmaceutical | textile | plastic extrusion | polythene bag converting<br>
      laminating and the food industries
    </p>
  </article>
</body>
</html>
```